CBD online business for pets and pet parents needs a new website

We need a website for my new online business. I have left a job of 25 years to do my passion. Helping Pets Live healthy and happy lives. I would like to provide my story so that our customer will know why I have started this business-To help!We will be providing all natural CBD (Hemp) products, specialty items, memorials as well as some products for pet parents. We would like our landing page to have our mission, be informative and easy to navigate and maybe feature our treats and oils for pets. We will need a page for pet products, a page for pet memorials, a page for pet lover products and a page for pet parent products.

Target Market(s)

millennials, boomers, pet lovers

Coding

Coded - Design and coding required

Number of Pages Required

5+ page

Colors
33b8a4

Requirements
Nice to have
• diagram of hemp oil extract benefits for dogs and people

```html
<!DOCTYPE html>
<html lang="en">
<head>
<meta charset="utf-8">
<title>Tailwell Haven — Natural care for pets</title>
<link rel="stylesheet" href="https://fonts.googleapis.com/css2?family=Open+Sans:wght@400;600&family=Caveat:wght@700&display=swap">
<style>
:root{
  --teal:#33b8a4;
  --teal-soft:#66ccbb;
  --ink:#1f1f1f;
  --muted:#6b6b6b;
  --white:#ffffff;
  --gold:#f7d96b;
  --grey-btn:#8f8f8f;
  --sans:'Open Sans',sans-serif;
  --script:'Caveat',cursive;
}
*{box-sizing:border-box;margin:0;padding:0}
html,body{width:1200px;height:2989px;overflow:hidden;background:var(--white);font-family:var(--sans);color:var(--ink)}
.page{position:relative;width:1200px;height:2989px}
.abs{position:absolute}

/* header */
.top-rule{left:0;top:40px;width:1200px;height:2px;background:var(--teal);opacity:.8}
.brand{left:86px;top:52px;width:150px;height:70px;background:var(--white);display:flex;align-items:center;gap:8px;padding-left:8px}
.brand-dot{width:16px;height:16px;border-radius:50%;background:var(--teal)}
.brand-name{font-size:18px;font-weight:600;color:var(--teal);line-height:1.1}
.shapes{left:886px;top:8px}
.login{left:1097px;top:10px;font-size:18px;color:var(--teal)}
.nav a{position:absolute;top:76px;font-size:19px;color:var(--muted);text-decoration:none}
.nav .active{color:var(--muted)}
.nav-underline{left:700px;top:112px;width:84px;height:4px;background:var(--teal)}
.cart-badge{left:1014px;top:65px;width:44px;height:44px;border-radius:50%;background:var(--teal);color:var(--white);font-size:17px;font-weight:600;display:flex;align-items:center;justify-content:center}
.dropdown{left:700px;top:118px;width:240px;height:155px;background:var(--white);box-shadow:0 2px 6px rgba(0,0,0,.15);z-index:5}
.dropdown span{position:absolute;left:20px;font-size:19px;color:var(--muted)}

/* hero */
.hero-photo{left:0;top:147px;width:1200px;height:652px;background:linear-gradient(110deg,#4a4a48 0%,#6e6d69 45%,#3c3c3a 70%,#7d8d5f 100%)}
.hero-title{left:122px;top:320px;font-family:var(--script);font-size:56px;line-height:74px;color:var(--gold)}
.hero-card{left:800px;top:183px;width:367px;height:459px;background:var(--white)}
.bottle{background:linear-gradient(180deg,#2a1d16 0%,#3b2a20 45%,#f2f2f2 46%,#ffffff 80%,#3b2a20 100%);border-radius:12px 12px 8px 8px}
.hero-bottle{left:124px;top:45px;width:110px;height:315px}
.btn-shop{left:84px;top:365px;width:203px;height:57px;background:var(--teal);color:var(--white);font-size:19px;display:flex;align-items:center;justify-content:center;box-shadow:0 2px 4px rgba(0,0,0,.2)}

/* popular */
.popular-bg{left:32px;top:723px}
.popular-title{left:32px;top:758px;width:1135px;text-align:center;font-size:32px;font-weight:600;color:var(--white)}
.product{top:848px;height:331px;background:var(--white)}
.product .bottle{position:absolute;left:50%;top:35px;width:70px;height:200px;margin-left:-35px}
.product-name{position:absolute;left:32px;top:262px;font-size:19px;font-weight:600}
.product-price{position:absolute;left:32px;top:290px;font-size:18px;font-weight:600}
.overlay-btn{position:absolute;left:0;width:100%;height:62px;background:var(--grey-btn);color:var(--white);font-size:19px;font-weight:600;display:flex;align-items:center;justify-content:center;opacity:.95}

/* story blocks */
.h-section{font-size:32px;font-weight:400;line-height:1.1}
.h-script{font-family:var(--script);font-size:38px;line-height:1;margin-top:-4px}
.para{font-size:19px;line-height:27px;margin-top:24px;width:500px}
.passion{left:50px;top:1378px}
.passion .h-script{color:var(--teal)}
.photo-friends{left:620px;top:1355px;width:547px;height:365px;background:linear-gradient(120deg,#c9b9a6,#e8dfd4 55%,#b8a48c)}
.teal-band{left:0;top:1771px;width:1200px;height:436px;background:var(--teal)}
.photo-cat{left:50px;top:1834px;width:465px;height:311px;background:radial-gradient(circle at 45% 55%,#b7a79a 0%,#6f7d5b 55%,#2f4a2a 100%)}
.healing{left:642px;top:1848px;color:var(--white)}
.healing .h-script{color:#1c2b29}

/* categories */
.cat-title{left:0;top:2258px;width:1200px;text-align:center;font-size:32px;font-weight:600}
.category{top:2343px;height:345px;background:var(--white);box-shadow:0 1px 4px rgba(0,0,0,.12)}
.category .cat-photo{position:absolute;left:0;top:0;width:100%;height:245px}
.category .cat-label{position:absolute;left:0;top:280px;width:100%;text-align:center;font-size:25px;font-weight:600}
.cat-pet .cat-photo{background:linear-gradient(135deg,#3aa695,#47b8a6)}
.cat-pet{background:var(--teal-soft)}
.cat-pet .cat-label{color:#2e8f80;font-weight:400}
.cat-visit{position:absolute;left:0;top:155px;width:100%;text-align:center;font-size:30px;font-weight:600;color:var(--white)}
.cat-lover .cat-photo{background:linear-gradient(120deg,#3b3532,#8c7e72 50%,#2a2421)}
.cat-parent .cat-photo{background:linear-gradient(120deg,#3d5a2c,#c27a3c 50%,#4a3a26)}

/* footer */
.foot-rule{left:0;top:2771px;width:1200px;height:2px;background:var(--teal)}
.foot-links a{position:absolute;font-size:19px;color:var(--muted);text-decoration:none}
.copyright{left:0;top:2936px;width:1200px;height:53px;background:var(--teal);color:var(--white);font-size:17px;display:flex;align-items:center;justify-content:center}
</style>
</head>
<body>
<div class="page">

  <header>
    <div class="abs top-rule"></div>
    <div class="abs brand"><span class="brand-dot"></span><span class="brand-name">Tailwell Haven</span></div>
    <svg class="abs shapes" width="86" height="22" viewBox="0 0 86 22" aria-hidden="true">
      <rect x="0" y="2" width="18" height="18" fill="#33b8a4"/>
      <circle cx="37" cy="11" r="10" fill="#33b8a4"/>
      <polygon points="58,20 70,2 82,20" fill="#33b8a4"/>
    </svg>
    <div class="abs login">Login</div>
    <nav class="nav">
      <a href="#" style="left:455px">Home</a>
      <a href="#" style="left:558px">Memorials</a>
      <a href="#" class="active" style="left:700px">Shop all</a>
      <a href="#" style="left:825px">Account</a>
      <a href="#" style="left:947px">Cart</a>
    </nav>
    <div class="abs nav-underline"></div>
    <div class="abs cart-badge">2</div>
    <div class="abs dropdown">
      <span style="top:20px">Pet products</span>
      <span style="top:61px">Pet lover products</span>
      <span style="top:105px">Pet parent products</span>
    </div>
  </header>

  <section>
    <div class="abs hero-photo" role="img" aria-label="Photo of an older dog resting its head on a wooden deck"></div>
    <h1 class="abs hero-title" style="font-weight:700">Helping Pets Live healthy<br>and happy lives</h1>
    <div class="abs hero-card">
      <div class="abs bottle hero-bottle" role="img" aria-label="Photo of a dropper bottle of pet oil"></div>
      <div class="abs btn-shop">Shop now</div>
    </div>
  </section>

  <section>
    <svg class="abs popular-bg" width="1135" height="584" viewBox="0 0 1135 584" aria-hidden="true">
      <polygon points="0,0 1135,0 1135,501 586,584 0,501" fill="#33b8a4"/>
    </svg>
    <h2 class="abs popular-title">Popular products</h2>
    <div class="abs product" style="left:50px;width:349px">
      <div class="bottle" role="img" aria-label="Photo of a dropper bottle of pet oil"></div>
      <div class="overlay-btn" style="top:194px">Add to cart</div>
      <div class="overlay-btn" style="top:269px">More details</div>
    </div>
    <div class="abs product" style="left:415px;width:368px">
      <div class="bottle" role="img" aria-label="Photo of a dropper bottle of pet oil"></div>
      <div class="product-name">Calm Tails CBD 14mg</div>
      <div class="product-price">$15.99</div>
    </div>
    <div class="abs product" style="left:798px;width:349px">
      <div class="bottle" role="img" aria-label="Photo of a dropper bottle of pet oil"></div>
      <div class="product-name" style="left:33px">Calm Tails CBD 20mg</div>
      <div class="product-price" style="left:33px">$19.99</div>
    </div>
  </section>

  <section>
    <div class="abs passion">
      <h2 class="h-section">Pets are our passion</h2>
      <div class="h-script">Our impact</div>
      <p class="para">Lorem ipsum dolor sit amet, consectetur adipiscing elit. Pellentesque pulvinar egestas turpis sit amet tincidunt. Phasellus sit amet neque non risus vehicula aliquet sit amet non diam. Integer sem massa, lacinia eget rutrum et, condimentum eget nunc.</p>
    </div>
    <div class="abs photo-friends" role="img" aria-label="Photo of a woman lying on the floor smiling at a fluffy puppy"></div>
  </section>

  <section>
    <div class="abs teal-band"></div>
    <div class="abs photo-cat" role="img" aria-label="Photo of a calico cat sitting outdoors among green leaves"></div>
    <div class="abs healing">
      <h2 class="h-section">Natural healing</h2>
      <div class="h-script">Safe, and effective</div>
      <p class="para" style="margin-top:20px">Lorem ipsum dolor sit amet, consectetur adipiscing elit. Pellentesque pulvinar egestas turpis sit amet tincidunt. Phasellus sit amet neque non risus vehicula aliquet sit amet non diam. Integer sem massa, lacinia eget rutrum et, condimentum eget nunc.</p>
    </div>
  </section>

  <section>
    <h2 class="abs cat-title">Categories</h2>
    <div class="abs category cat-pet" style="left:32px;width:367px">
      <div class="cat-photo" role="img" aria-label="Photo of a parrot under a teal tint"></div>
      <div class="cat-visit">Visit</div>
      <div class="cat-label">Pet products</div>
    </div>
    <div class="abs category cat-lover" style="left:415px;width:368px">
      <div class="cat-photo" role="img" aria-label="Photo of a senior dog in profile"></div>
      <div class="cat-label">Pet lover products</div>
    </div>
    <div class="abs category cat-parent" style="left:800px;width:367px">
      <div class="cat-photo" role="img" aria-label="Photo of a ginger cat lying in a garden"></div>
      <div class="cat-label">Pet parent products</div>
    </div>
  </section>

  <footer>
    <div class="abs foot-rule"></div>
    <div class="foot-links">
      <a href="#" style="left:50px;top:2792px">Home</a>
      <a href="#" style="left:51px;top:2831px">Memorials</a>
      <a href="#" style="left:440px;top:2792px">Shop all</a>
      <a href="#" style="left:443px;top:2831px">Account</a>
      <a href="#" style="left:600px;top:2792px">Privacy policy</a>
      <a href="#" style="left:600px;top:2831px">Contact</a>
    </div>
    <div class="abs copyright">2019 @ Tailwell Haven</div>
  </footer>

</div>
</body>
</html>
```